Elegantes und hochwertiges Etiketten-Design für Weinflasche
tulpenwerk hat unsere Anforderungen super umgesetzt und durch eine unkomplizierte und einfache Kommunikation konnten die Feinarbeiten schnell durchgeführt werden. Klasse Arbeit! Gerne wieder :)
Zielgruppe
Wir sind ein liebevoll geführter Familienwinzerbetrieb im schönen Franken, ohne lange Tradition, dafür jung, dynamisch, modern und voller Ideen. Von den eigenen Rebflächen produzieren wir unsere eigenen Weine.
Verantwortlich für den Weinan- und ausbau ist Matthias, stolzer Familienvater und leidenschaftlicher Hobbywinzer. Unterstützt wird er von seiner Familie, von der Verwandtschaft und von seinen Freunden.
Matthias ist hauptberuflich Elektroingenieur, Jongleur von Bits und Bytes. Der Ausgleich zum Beruf ist die Arbeit und Ruhe im Weinberg, immer mit dem Drang, etwas Handwerkliches mit den eigenen Händen umzusetzen.
Was hinter dem Weinausbau steckt ist pure Leidenschaft, Passion zur Perfektion, die Liebe zum Wein und das viele Probieren und Tüfteln im Weinberg und im Weinkeller. Und es ist diese Leidenschaft, die uns immer wieder neu motiviert. Dabei haben wir unser Ziel immer fest im Blick, individuelle Weine, Weine die unsere Handschrift tragen und sehr viel Fruchtpotential und Wiedererkennungswert aufweisen, zu erzeugen.
Zielgruppe:
Genussmenschen, die gerne fruchtige, unkomplizierte und mit unserer Handschrift geprägte Weine genießen wollen.
Aufgabenstellung
- Die Weinflasche (vor allem das Etikett) soll im Weinregal positiv ins Auge stechen und die Aufmerksamkeit des Weingenießer auf die Flasche lenken, aber gleichzeitig elegant und hochwertig wirken. Das Etikett soll beim Weingenießer Emotionen wecken und im Gedächtnis bleiben.
- Als Schlagwort soll „Herzgewitter“ und die Rebsorte „Bacchus“ auf die Vorderseite des Etiketts gedruckt werden. Das Schlagwort soll dabei im Fokus stehen. „Herzgewitter“ steht für die Liebe zwischen mir und meiner Frau, verkörpert in diesem frischen, fruchtigen und lebendigen Bacchus. Da wir dieses Jahr heiraten werden, möchten wir gerne anderen Menschen durch diesen besonderen Wein an unseren „Herzgewitter“ teilhaben lassen
- Im Hintergrund des Etiketts soll ein Bild von mir und meiner Frau als schwarz/weiß Kontur abgebildet sein.
- Das Etikett soll später eventuell mit einer Heißfolienprägung veredelt werden (z.B. Folienprägung von Schlagwort „Herzgewitter“).
- Das Etikett wird in Digitaldruck auf Selbstklebeetiketten gedruckt.
- Flaschenform: Schlegelflasche antikgrün
- Kapsel: schwarzer BVS-Verschluss

```html
<!DOCTYPE html>
<html lang="de">
<head>
<meta charset="utf-8">
<title>Herzgewitter – Bacchus Etikett</title>
<link rel="stylesheet" href="https://fonts.googleapis.com/css2?family=Cabin:ital,wght@0,400;0,500;0,600;0,700;1,400&family=Caveat+Brush&family=Rosarivo&display=swap">
<style>
  :root{
    --page:#ffffff;
    --label-paper:#ffffff;
    --peach:#f8c9b0;
    --heart:#2b2a28;
    --gold:#c9a33a;
    --gold-text:#b8862a;
    --ink:#1d1d1b;
    --rule:#8a7a70;
  }
  *{margin:0;padding:0;box-sizing:border-box}
  html,body{width:1200px;height:1112px;overflow:hidden;background:var(--page)}
  .canvas{position:relative;width:1200px;height:1112px}
  .label{
    position:absolute;left:50px;top:304px;width:1100px;height:504px;
    background:var(--label-paper);
    box-shadow:0 4px 10px rgba(0,0,0,.18);
  }
  .label__field{position:absolute;left:12px;top:12px;right:14px;bottom:17px;background:var(--peach)}
  .label__art{position:absolute;left:0;top:0;width:1100px;height:504px}
  .slogan{
    position:absolute;left:318px;top:52px;width:330px;
    font-family:"Caveat Brush",cursive;font-weight:400;color:#fff;line-height:.9;
  }
  .slogan__line{display:block;font-size:76px;white-space:nowrap}
  .slogan__line--second{padding-left:96px}
  .variety{
    position:absolute;left:415px;top:232px;
    font-family:"Rosarivo",serif;font-size:28px;color:var(--gold);
  }
  .info{
    position:absolute;left:782px;top:30px;width:270px;text-align:center;
    font-family:"Cabin",sans-serif;color:var(--ink);
  }
  .brand{display:flex;align-items:center;justify-content:center;gap:10px;height:100px}
  .brand__name{font-size:30px;font-weight:500;letter-spacing:.5px}
  .brand__dot{width:22px;height:22px;border-radius:50%;background:var(--gold)}
  .wine{font-size:18px;font-weight:600;line-height:23px;margin-top:22px}
  .quality{font-size:17px;line-height:22px;margin-top:4px}
  .apnr{font-size:14px;line-height:18px}
  .rule{height:1px;background:var(--rule);width:253px;margin:18px auto 0}
  .bottler-tag{font-size:16px;font-style:italic;letter-spacing:1px;margin-top:20px}
  .bottler{font-size:18px;font-weight:600;letter-spacing:1px;margin-top:8px}
  .address{font-size:17px;line-height:22px}
  .web{font-size:17px;font-weight:700;color:var(--gold-text);margin-top:2px}
  .volume,.alcohol{position:absolute;top:450px;font-family:"Cabin",sans-serif;font-size:22px;font-weight:600;color:var(--ink)}
  .volume{left:758px}
  .alcohol{left:968px}
</style>
</head>
<body>
<div class="canvas">
  <section class="label">
    <div class="label__field"></div>
    <svg class="label__art" viewBox="0 0 1100 504">
      <defs>
        <radialGradient id="rayGlow" cx="0.5" cy="0.5" r="0.5">
          <stop offset="0" stop-color="#c9a33a" stop-opacity=".55"/>
          <stop offset="1" stop-color="#c9a33a" stop-opacity="0"/>
        </radialGradient>
        <linearGradient id="coupleTone" x1="0" y1="0" x2="0" y2="1">
          <stop offset="0" stop-color="#faf6f2" stop-opacity=".45"/>
          <stop offset="1" stop-color="#ffffff"/>
        </linearGradient>
      </defs>
      <ellipse cx="480" cy="200" rx="360" ry="290" fill="url(#rayGlow)" role="img" aria-label="Goldene Strahlen, die vom Herz nach außen leuchten"/>
      <rect x="0" y="12" width="437" height="492" fill="url(#coupleTone)" role="img" aria-label="Schwarz-weiße Konturzeichnung des Winzerpaares"/>
      <path transform="translate(287 26)" fill="#2b2a28"
        d="M190 311 C90 250 0 175 4 95 C8 30 70 2 125 10 C160 16 180 35 190 55 C202 30 235 2 290 2 C350 4 382 55 376 118 C368 200 280 255 190 311 Z"/>
    </svg>
    <h1 class="slogan"><span class="slogan__line">Herz-</span><span class="slogan__line slogan__line--second">gewitter</span></h1>
    <p class="variety">Bacchus</p>
    <div class="info">
      <div class="brand"><span class="brand__name">Weinbau Kessler</span><span class="brand__dot"></span></div>
      <p class="wine">Franken 2018er<br>Bacchus<br>Q.b.A. feinfruchtig</p>
      <p class="quality">Deutscher Qualitätswein</p>
      <p class="apnr">A.P.Nr. 4127-015-19 – Enthält Sulfite</p>
      <div class="rule"></div>
      <p class="bottler-tag">– Abfüller –</p>
      <p class="bottler">WEINBAU KESSLER</p>
      <p class="address">Lindenweg 7 · D-97199 Sommerau<br>Telefon 09341 – 2790</p>
      <p class="web">www.weinbau-kessler.de</p>
    </div>
    <p class="volume">0,75 l</p>
    <p class="alcohol">11,5 % vol</p>
  </section>
</div>
</body>
</html>
```